Trade fair PLAMX business card 7” x 5”

PLAMX exhibits on technology-hospitality trade fair in the UK this year. Therefore we are looking for well-designed marketing card (examples are linked in the bottom). The main role of these materials is to attract receivers to visit our website & find out more about PLAMX solutions.
Preferred used colours: white, various blue tints, black.
The front should contain branding & motto (“Modern beverage stocktaking”). Logotypes are attached.
The back should contain:
(value proposition),
Modern technology solution for beverage stocktaking
Accurate & effective stocktaking
Swift measuring with 99% accuracy makes stocktaking significantly quicker and more cost effective (or cost optimising).
Software solution supported with/by hardware tools
PLAMX system is based on universally accessible platforms - smartphones, PCs, and laptops. Your main measuring tool, smart scale, is delivered by PLAMX.
Smart & simple reporting system
Data availability - everywhere, anytime
Useful functions help stock managing at your bar
(call to action),
Find us on plamx-vend.com and try PLAMX with a one-month free trial.
(promo code)
Claim your 50% off discount with above promo code
Marketing card examples:
https://www.vendrilosa.com/Which-startup-has-the-best-brochure-in-terms-of-design-and-content
PLAMX solution was created to help bar owners, bar managers and head bartenders to make their stocktaking process swift & accurate. Therefore, our product is targeting every business which sells portioned beverages.
Information Technology

```html
<!DOCTYPE html>
<html lang="en">
<head>
<meta charset="utf-8">
<title>PLAMX – Trade fair card</title>
<link rel="stylesheet" href="https://fonts.googleapis.com/css2?family=Lato:wght@400;700&family=Roboto:wght@500;700;900&family=Poiret+One&display=swap">
<style>
  :root {
    --page: #e9ebee;
    --night: #14141f;
    --night-deep: #0b0b12;
    --plum: #2e1f3a;
    --blue: #3a7fc4;
    --blue-bright: #3d8ad8;
    --blue-text: #4a8fd6;
    --white: #ffffff;
    --grey-bar: #6e6e6e;
    --ink: #222a33;
    --suit: #3b3b40;
  }
  * { box-sizing: border-box; margin: 0; padding: 0; }
  html, body { width: 1200px; height: 1200px; overflow: hidden; }
  body { background: var(--page); position: relative; font-family: "Lato", sans-serif; color: var(--white); }

  .card { position: absolute; left: 246px; width: 712px; height: 508px; overflow: hidden; background: var(--white); box-shadow: 0 6px 18px rgba(0,0,0,.25); }
  .card--front { top: 67px; }
  .card--back { top: 618px; }

  /* front */
  .front__scene { position: absolute; left: 0; top: 0; width: 712px; height: 465px;
    background: radial-gradient(ellipse at 30% 35%, var(--plum) 0%, var(--night) 55%, var(--night-deep) 100%); }
  .front__person { position: absolute; left: 378px; top: 25px; width: 334px; height: 483px;
    background: linear-gradient(180deg, #c49a70 0%, #b48a64 18%, var(--suit) 38%, #2c2c31 100%);
    border-radius: 140px 120px 0 0; }
  .front__band { position: absolute; left: 0; top: 465px; width: 712px; height: 36px; background: var(--blue); }
  .front__url { position: absolute; left: 90px; top: 475px; font-family: "Roboto", sans-serif; font-weight: 500; font-size: 13px; letter-spacing: 7px; }
  .brand { position: absolute; left: 42px; top: 58px; display: flex; align-items: center; gap: 14px; }
  .brand__mark { width: 44px; height: 44px; background: var(--blue-bright); }
  .brand__name { font-family: "Roboto", sans-serif; font-weight: 900; font-size: 66px; line-height: 1; color: var(--white); }
  .motto { position: absolute; left: 30px; top: 220px; font-family: "Roboto", sans-serif; font-weight: 700; }
  .motto__lead { font-size: 41px; color: var(--blue-text); line-height: 1.2; }
  .motto__main { font-size: 47px; color: var(--white); line-height: 1.2; letter-spacing: .5px; }

  /* back */
  .back__scene { position: absolute; left: 0; top: 0; width: 712px; height: 266px;
    background: linear-gradient(180deg, #1a1418 0%, #4a2e22 35%, #3a2620 62%, var(--night-deep) 70%, #1a1016 100%); }
  .back__headline { position: absolute; left: 0; top: 168px; width: 712px; text-align: center; }
  .back__headline-light { font-family: "Poiret One", sans-serif; font-size: 40px; line-height: 1.05; }
  .back__headline-bold { font-family: "Roboto", sans-serif; font-weight: 900; font-size: 31px; line-height: 1.2; }
  .panel { position: absolute; left: 0; top: 266px; width: 712px; height: 192px; background: var(--blue); }
  .features { position: absolute; left: 29px; top: 280px; width: 400px; }
  .features__title { font-weight: 700; font-size: 14.5px; margin-bottom: 14px; }
  .features__list { list-style: none; font-size: 12px; }
  .features__list li { position: relative; padding-left: 15px; margin-bottom: 11px; line-height: 1.3; }
  .features__list li::before { content: ""; position: absolute; left: 1px; top: 4px; width: 7px; height: 7px; border-radius: 50%; background: var(--white); }

  .promo { position: absolute; left: 432px; top: 280px; width: 252px; height: 66px; background: var(--white);
    border-radius: 14px; box-shadow: inset 0 0 0 2px #cfd8e2; color: var(--ink); padding: 9px 12px 0; }
  .promo__title { font-family: "Roboto", sans-serif; font-weight: 500; font-size: 22px; line-height: 1; color: #3a3a3a; }
  .promo__title b { color: var(--blue-bright); font-weight: 700; }
  .promo__note { font-size: 14px; margin-top: 5px; }

  .benefit { position: absolute; left: 432px; top: 358px; width: 252px; height: 87px; border: 1.5px solid var(--white); border-radius: 12px; padding: 5px 14px 0; }
  .benefit__title { font-weight: 700; font-size: 13.5px; text-align: justify; text-align-last: justify; padding-bottom: 3px; border-bottom: 1px solid rgba(255,255,255,.7); }
  .benefit__text { font-size: 13.5px; line-height: 1.3; text-align: justify; text-align-last: justify; margin-top: 3px; }

  .footer { position: absolute; left: 0; top: 461px; width: 712px; height: 40px; background: var(--grey-bar);
    display: flex; align-items: center; justify-content: center; gap: 5px; font-size: 15.5px; }
  .footer__label { font-weight: 700; }
  .footer__link { background: var(--white); color: #555; border-radius: 8px; padding: 0 4px; line-height: 1.15; }
</style>
</head>
<body>

<section class="card card--front">
  <div class="front__scene" role="img" aria-label="Dimly lit bar with shelves of bottles in the background"></div>
  <div class="brand">
    <span class="brand__mark"></span>
    <span class="brand__name">PLAMX</span>
  </div>
  <h1 class="motto">
    <span class="motto__lead">Modern beverage</span><br>
    <span class="motto__main">STOCKTAKING</span>
  </h1>
  <div class="front__band"></div>
  <p class="front__url">WWW.PLAMX-VEND.COM</p>
  <div class="front__person" role="img" aria-label="Smiling man in a dark suit checking a smartphone"></div>
</section>

<section class="card card--back">
  <div class="back__scene" role="img" aria-label="Row of spirit bottles on a backlit bar shelf"></div>
  <h2 class="back__headline">
    <span class="back__headline-light">Modern technology solution</span><br>
    <span class="back__headline-bold">FOR BEVERAGE STOCKTAKING</span>
  </h2>
  <div class="panel"></div>

  <div class="features">
    <p class="features__title">Software solution supported with/by hardware tools:</p>
    <ul class="features__list">
      <li>PLAMX system is based on universally accessible<br>platforms - smartphones, PCs, and laptops.</li>
      <li>Your main measuring tool, smart scale, is delivered by PLAMX.</li>
      <li>Smart &amp; simple reporting system</li>
      <li>Data availability - everywhere, anytime</li>
      <li>Useful functions help stock managing at your bar</li>
    </ul>
  </div>

  <div class="promo">
    <p class="promo__title">CLAIM YOUR <b>50%</b> OFF</p>
    <p class="promo__note">discount with above promo code</p>
  </div>

  <div class="benefit">
    <p class="benefit__title">Accurate &amp; effective stocktaking</p>
    <p class="benefit__text">Swift measuring with <b>99%</b> accuracy makes stocktaking significantly quicker and more cost effective.</p>
  </div>

  <div class="footer">
    <span class="footer__label">Find us on:</span>
    <svg width="20" height="20" viewBox="0 0 20 20" aria-hidden="true" fill="none" stroke="#fff" stroke-width="1.4">
      <circle cx="10" cy="10" r="8"/>
      <ellipse cx="10" cy="10" rx="3.5" ry="8"/>
      <path d="M2 10h16M3.5 6h13M3.5 14h13"/>
    </svg>
    <span class="footer__link">www.plamx-vend.com</span>
    <span>and try PLAMX with a one-month free trial</span>
  </div>
</section>

</body>
</html>
```